Classy business card for accounting firm

We're looking for a new business card for our accounting firm. Our logo was designed by Brandloom, so all of the design info we would like to use has been provided. The specific font provided isn't required to be used.

We want the card to look classy and elegent. Probably more minimalistic, but still with some pops of color.

The options we would like to include on the card are as follows:
1. Main office phone line
2. Direct phone line
3. Email address
4. Website URL
5. Name
6. Title (CEO, President, etc.)
7. Firm Address

The design and card should be double sided!!! The drop down box in the project brief for some reason is defaulting to single sided. Not sure why this is happening.

Thanks!

Contact Information for Business Card

The options we would like to include on the card are as follows: 1. Main office phone line 2. Direct phone line 3. Email address 4. Website URL 5. Name 6. Title (CEO, President, etc.) 7. Firm Address

Requirements
Must have
• Card must be double sided.

```html
<!DOCTYPE html>
<html lang="en">
<head>
<meta charset="UTF-8">
<title>Ledgerline Associates – Business Card</title>
<link rel="stylesheet" href="https://fonts.googleapis.com/css2?family=Montserrat:wght@400;500;600;700&display=swap">
<style>
  :root {
    --orange: #f47c20;
    --green: #a8c43a;
    --ink: #222222;
    --grey: #555a5e;
    --white: #ffffff;
    --backdrop: #e9e7e4;
  }
  * { margin: 0; padding: 0; box-sizing: border-box; }
  html, body { width: 1200px; height: 900px; overflow: hidden; }
  body {
    background: var(--backdrop);
    font-family: "Montserrat", Arial, sans-serif;
    position: relative;
  }
  .card {
    position: absolute;
    left: 250px;
    width: 700px;
    height: 400px;
    overflow: hidden;
    box-shadow: 0 6px 18px rgba(0,0,0,0.18);
  }
  .card--front { top: 36px; background: var(--orange); color: var(--white); }
  .card--back { top: 464px; background: var(--white); color: var(--ink); }

  /* Front */
  .front-brand {
    position: absolute; inset: 0;
    display: flex; flex-direction: column; align-items: center; justify-content: center;
  }
  .front-brand .brand-mark {
    width: 26px; height: 26px; background: var(--white); margin-bottom: 26px;
  }
  .front-brand .brand-name {
    font-size: 40px; font-weight: 600; letter-spacing: 3px; white-space: nowrap;
  }
  .tagline {
    display: flex; align-items: center; gap: 14px; margin-top: 8px;
    font-size: 15px; font-weight: 500; letter-spacing: 4px; white-space: nowrap;
  }
  .tagline .rule { width: 110px; height: 2px; background: currentColor; }

  /* Back */
  .back-brand {
    position: absolute; left: 168px; top: 48px;
    display: flex; align-items: center; gap: 16px;
  }
  .back-brand .brand-mark { width: 22px; height: 22px; background: var(--orange); flex: none; }
  .back-brand .brand-name {
    font-size: 26px; font-weight: 600; letter-spacing: 2px; color: var(--grey); white-space: nowrap;
  }
  .back-brand .tagline {
    font-size: 10px; letter-spacing: 3px; color: var(--grey); margin-top: 4px; justify-content: center;
  }
  .back-brand .tagline .rule { width: 70px; background: var(--green); }

  .person {
    position: absolute; left: 40px; top: 138px; width: 270px; text-align: right;
  }
  .person .name { font-size: 24px; font-weight: 700; letter-spacing: 1px; white-space: nowrap; }
  .person .name .first { color: var(--green); }
  .person .name .last { color: var(--orange); }
  .person .title { font-size: 15px; font-weight: 500; margin: 4px 0 10px; }
  .person .address { font-size: 14px; font-weight: 500; line-height: 1.4; font-style: normal; white-space: nowrap; }

  .divider {
    position: absolute; left: 330px; top: 136px; width: 2px; height: 110px; background: var(--green);
  }
  .contacts {
    position: absolute; left: 350px; top: 134px; list-style: none;
  }
  .contacts li {
    display: flex; align-items: center; gap: 10px;
    font-size: 14px; font-weight: 500; height: 28px; white-space: nowrap;
  }
  .contacts svg { width: 16px; height: 16px; fill: var(--orange); flex: none; }

  .swoosh { position: absolute; left: 0; top: 0; width: 700px; height: 400px; }
</style>
</head>
<body>

  <section class="card card--front" aria-label="Card front">
    <div class="front-brand">
      <span class="brand-mark"></span>
      <div class="brand-name">LEDGERLINE ASSOCIATES</div>
      <div class="tagline"><span class="rule"></span>SOLVING TAX PROBLEMS<span class="rule"></span></div>
    </div>
  </section>

  <section class="card card--back" aria-label="Card back">
    <svg class="swoosh" viewBox="0 0 700 400" aria-hidden="true">
      <path d="M0 400 L0 355 C320 350 560 320 700 240 L700 400 Z" fill="var(--orange)"/>
      <path d="M120 340 C360 336 580 298 688 226" fill="none" stroke="var(--green)" stroke-width="4" stroke-linecap="round"/>
    </svg>

    <div class="back-brand">
      <span class="brand-mark"></span>
      <div>
        <div class="brand-name">LEDGERLINE ASSOCIATES</div>
        <div class="tagline"><span class="rule"></span>SOLVING TAX PROBLEMS<span class="rule"></span></div>
      </div>
    </div>

    <div class="person">
      <div class="name"><span class="first">MARCUS</span> <span class="last">HALE</span></div>
      <div class="title">CEO, President</div>
      <address class="address">Northgate Plaza 4500 Park<br>Elmwood Ave Suite 202</address>
    </div>

    <div class="divider"></div>

    <ul class="contacts">
      <li><svg viewBox="0 0 16 16"><path d="M2 5c0-2 2-3 6-3s6 1 6 3v1h-3V5H5v1H2zM3 8l2-2h6l2 2v6H3z"/></svg>555-210-4789</li>
      <li><svg viewBox="0 0 16 16"><path d="M4 1h8v14H4zM5.5 3v9h5V3zM7 13h2v1H7z" fill-rule="evenodd"/></svg>555-382-5609</li>
      <li><svg viewBox="0 0 16 16"><path d="M1 3h14v10H1zM2 4l6 5 6-5z" fill-rule="evenodd"/></svg>info@ledgerlineassoc.com</li>
      <li><svg viewBox="0 0 16 16"><circle cx="8" cy="8" r="7"/></svg>www.ledgerlineassoc.com</li>
    </ul>
  </section>

</body>
</html>
```